Speisekarten für ein Seerestaurant/Pizzeria
Zielgruppe
Wir sin ein Seerestaurant/Pizzeria in einem Ferien Ort
Aufgabenstellung
Wir brauchen Speisekarte in A4 und A5 Format und wichtig dass wir das Inhalt immer einfach bearbeiten können

```html
<!DOCTYPE html>
<html lang="de">
<head>
<meta charset="utf-8">
<title>Ufli – Speisekarte</title>
<link rel="stylesheet" href="https://fonts.googleapis.com/css2?family=Oswald:wght@500&family=Barlow+Condensed:wght@300;400&family=Montserrat:wght@600&family=Open+Sans:ital,wght@0,700;1,400&display=swap">
<style>
:root{
  --stage:#dcdcde;
  --cream:#f4efe0;
  --cream-shade:#e9e4d3;
  --ink:#373833;
  --paper:#ffffff;
  --light:#f4efe0;
  --rule:#6b6c66;
}
*{box-sizing:border-box;margin:0;padding:0}
html,body{width:1200px;height:2296px;overflow:hidden}
body{background:var(--stage);position:relative;font-family:"Barlow Condensed",sans-serif;color:var(--ink)}
.band{position:absolute;left:0;top:1400px;width:1200px;height:40px;background:var(--paper)}

/* ---------- cover ---------- */
.cover{position:absolute;width:357px;height:505px;background:var(--cream);overflow:hidden;transform-origin:0 0}
.cover .dark{position:absolute;left:28px;top:91px;width:329px;height:381px;background:var(--ink)}
.cover .photo{position:absolute;left:0;top:123px;width:327px;height:265px;
  background:linear-gradient(160deg,#8a8a80 0%,#c8a27a 35%,#e2b870 55%,#b85a2c 75%,#3b3a36 100%)}
.cover .brand-box{position:absolute;left:117px;top:0;width:121px;height:172px;background:var(--cream);
  display:flex;flex-direction:column;align-items:center;justify-content:flex-end;padding-bottom:10px}
.brand-name{font-family:"Oswald",sans-serif;font-weight:500;color:var(--ink);line-height:1}
.cover .brand-name{font-size:38px}
.cover .brand-sub{font-size:6px;margin-top:5px;letter-spacing:.1px}
.cover .title{position:absolute;left:28px;width:329px;top:414px;text-align:center;color:var(--light);
  font-family:"Barlow Condensed",sans-serif;font-weight:300;font-size:11.5px;letter-spacing:2.6px;line-height:17px}
.cover .footer{position:absolute;top:480px;left:0;width:357px;font-size:7px;letter-spacing:.9px}
.cover .footer .addr{position:absolute;left:132px}
.cover .footer .web{position:absolute;left:308px}

/* ---------- spread ---------- */
.spread{position:absolute;width:714px;height:505px;background:var(--paper);transform-origin:0 0}
.page{position:absolute;top:0;width:357px;height:505px}
.page.left{left:0}
.page.right{left:357px;background:linear-gradient(90deg,var(--cream-shade),var(--cream) 12%)}
.page.left .cream{position:absolute;left:0;top:27px;width:328px;height:478px;background:var(--cream)}
.page.right .top-strip{position:absolute;left:0;top:0;width:148px;height:27px;background:var(--paper)}
.page.right .edge{position:absolute;left:329px;top:470px;width:28px;height:35px;background:var(--paper)}
.page-brand{position:absolute;left:40px;top:45px;display:flex;align-items:center;gap:6px}
.page-brand .dot{width:14px;height:14px;border-radius:50%;background:var(--ink)}
.page-brand .brand-name{font-size:24px}
.page-brand .brand-sub{font-size:4.5px;margin-top:2px}

.card{position:absolute;left:29px;width:104px;background:var(--paper);text-align:center}
.card .pic{height:95px}
.card .name{font-size:8.5px;letter-spacing:.4px;margin-top:8px}
.card .desc{font-size:5.4px;line-height:7px;padding:0 5px}
.card .price{position:absolute;left:0;bottom:0;width:104px;height:17px;background:var(--ink);color:var(--light);
  font-family:"Open Sans",sans-serif;font-weight:700;font-size:4.6px;display:flex;flex-direction:column;align-items:center;justify-content:center;line-height:6px}
.note{position:absolute;left:40px;width:76px;top:409px;text-align:center;font-family:"Open Sans",sans-serif;font-style:italic;font-size:4.8px;line-height:7.5px}

.panel{position:absolute;left:149px;width:208px;background:var(--ink);color:var(--light);text-align:center;padding:22px 11px 0}
.panel h2{font-family:"Montserrat",sans-serif;font-weight:600;font-size:7.5px;letter-spacing:2.6px;line-height:11px;margin-bottom:9px}
.item{padding:4px 0 5px;border-bottom:.5px solid var(--rule);font-size:5.2px;line-height:7px}
.item:last-of-type{border-bottom:none}
.item b{font-weight:400;font-size:8.5px;letter-spacing:.4px}
.item .cost{display:block;font-family:"Open Sans",sans-serif;font-weight:700;font-size:4.4px;margin-top:2px}
.panel .foot{font-family:"Open Sans",sans-serif;font-style:italic;font-size:5px;line-height:7.5px;margin-top:14px}
</style>
</head>
<body>

<!-- ===== upper presentation ===== -->
<section class="cover" style="left:494px;top:165px">
  <div class="dark"></div>
  <div class="photo" role="img" aria-label="Foto: gedeckter Tisch am See mit Pasta, Pizza, Brotkorb und Rotwein"></div>
  <div class="brand-box">
    <div class="brand-name">Ufli</div>
    <div class="brand-sub">Seerestaurant – SEEBLICK – Seedorf</div>
  </div>
  <h1 class="title">Seerestaurant<br>SEEBLICK – Seedorf</h1>
  <div class="footer"><span class="addr">Uferweg 12 • 6000 Seedorf</span><span class="web">ufli-seedorf.ch</span></div>
</section>

<section class="spread" style="left:232px;top:733px">
  <div class="page left">
    <div class="cream"></div>
    <div class="page-brand"><span class="dot"></span><div><div class="brand-name">Ufli</div><div class="brand-sub">Seerestaurant – SEEBLICK – Seedorf</div></div></div>
    <article class="card" style="top:111px;height:150px">
      <div class="pic" role="img" aria-label="Foto: Gulaschsuppe im Topf mit Brot" style="background:linear-gradient(150deg,#d8c39a,#8a3a22 55%,#3e2a20)"></div>
      <div class="name">GULASCHSUPPE</div><div class="desc">...die Echte – nach ungarischer Art</div>
      <div class="price"><span>kl. Portion CHF 13.50</span><span>gr. Portion CHF 20.50</span></div>
    </article>
    <article class="card" style="top:270px;height:143px">
      <div class="pic" role="img" aria-label="Foto: Salatteller mit Pouletstreifen" style="background:linear-gradient(150deg,#7e9a4a,#d9a24e 50%,#e8d27a 75%,#6a7a3a)"></div>
      <div class="name">FITNESSTELLER</div><div class="desc">mit Pouletstreifen</div>
      <div class="price"><span>CHF 13.50</span></div>
    </article>
    <p class="note">Alle Salate mit hausgemachter Salatsauce Ihrer Wahl und frischem Pizzabrot</p>
    <div class="panel" style="top:111px;height:126px">
      <h2>SUPPEN</h2>
      <div class="item"><b>BOUILLON</b> mit Tortellini<span class="cost">CHF 10.50</span></div>
      <div class="item"><b>MINESTRONE</b><span class="cost">CHF 11.50</span></div>
      <div class="item"><b>TAGESSUPPE</b> fragen Sie unser Personal<span class="cost">CHF 11.50</span></div>
    </div>
    <div class="panel" style="top:245px;height:225px">
      <h2>SALATE</h2>
      <div class="item"><b>BURRATA</b> italienischer Frischkäse, mit frischem Basilikum,<br>extra natives Olivenöl, Balsamico Crema und Cherry Tomaten<span class="cost">CHF 10.50</span></div>
      <div class="item"><b>CEASAR SALAT</b> mit Speck, Croûtons und Parmigiano DOP<span class="cost">CHF 10.50</span></div>
      <div class="item"><b>GEMISCHTER SALAT</b><span class="cost">CHF 10.50</span></div>
      <div class="item"><b>GRÜNER SALAT</b><span class="cost">CHF 10.50</span></div>
      <div class="item"><b>NÜSSLISALAT</b> mit Speck, Brotcroûtons und Ei<span class="cost">CHF 10.50</span></div>
      <div class="item"><b>SALAT «SEEBLICK»</b> Eisberg Salat, Speck, Croutons,<br>Parmigiano DOP und Pouletstreifen<span class="cost">CHF 10.50</span></div>
    </div>
  </div>
  <div class="page right">
    <div class="top-strip"></div>
    <div class="edge"></div>
    <article class="card" style="top:111px;height:150px">
      <div class="pic" role="img" aria-label="Foto: Chicken-Fingers mit Pommes und Dip" style="background:linear-gradient(150deg,#e8d6b0,#e6a63a 45%,#c8722e 70%,#f1ece0)"></div>
      <div class="name">CHICKEN-FINGERS</div><div class="desc">hausgemachte, panierte Pouletstreifen, dazu sweet Chili-Sauce und Pommes Frites</div>
      <div class="price"><span>CHF 32.50</span></div>
    </article>
    <article class="card" style="top:270px;height:151px">
      <div class="pic" role="img" aria-label="Foto: Pulled Pork Burger mit Pommes" style="background:linear-gradient(150deg,#6b4a34,#c8642e 45%,#e2b060 70%,#8a5a3a)"></div>
      <div class="name">PULLED PORK Burger</div><div class="desc">hausgemachte Bun, Pulled Pork (180g), BBQ-Sauce, Cheddar-Käse, Coleslaw (Kabissalat) und Jalapeno, serviert mit Pommes</div>
      <div class="price"><span>CHF 28.50</span></div>
    </article>
    <div class="panel" style="top:0;height:237px">
      <h2>HAUPTGERICHTE</h2>
      <div class="item"><b>BEEFSTEAK TARTAR</b> aus Schweizer-Qualitätsrindfleisch<br>abgeschmeckt nach Ihrem Wunsch, serviert mit Toastbrot und Butter<span class="cost">Vorspeise CHF 22.50 &nbsp;|&nbsp; Hauptgang CHF 32.50</span></div>
      <div class="item"><b>CORDON BLEU</b> «das Klassische» vom Schwein,<br>gefüllt mit Vorderschinken, Raclette und würzigem Gruyère<br>serviert mit Pommes Frites und Gemüse<span class="cost">CHF 26.50</span></div>
      <div class="item"><b>GYROS-TELLER</b> mit Schweinefleisch serviert mit Salat-Bouquet,<br>Tzatziki-Sauce und Pommes Frites<span class="cost">CHF 30.50</span></div>
      <div class="item"><b>WIENER SCHNITZEL</b> vom Kalb mit Pommes Frites<br>und Preiselbeeren<span class="cost">CHF 35.50</span></div>
    </div>
    <div class="panel" style="top:245px;height:225px">
      <h2>BARBECUE SPEZIALITÄTEN<br>AUS DEM SMOKER</h2>
      <div class="item"><b>BBQ SPARE RIBS</b> aus dem Smoker mit Cherry-Bomb Glasur<br>serviert mit Pommes frites<span class="cost">CHF 44.00</span></div>
      <div class="item"><b>PULLED BEEF Burger</b> Hausgemachte Bun, Pulled Beef (180g),<br>BBQ-Sauce, Cheddar-Käse, Coleslaw (Kabissalat) und Jalapeno,<br>serviert mit Pommes<span class="cost">CHF 31.50</span></div>
      <div class="item"><b>PULLED VEGI Burger</b> Hausgemachte Bun, BBQ-Sauce,<br>Cheddar-Käse, Coleslaw (Kabissalat) und Jalapeno, serviert mit Pommes<span class="cost">CHF 25.50</span></div>
      <p class="foot">Barbecue Gerichte werden 6-12 Stunden im Smoker gegart.<br>Wir verwenden ausschliesslich Schweizer Fleisch und<br>Bio Hickory Holz für das typische BBQ-Erlebnis<br>und Rauch-Aroma.</p>
    </div>
  </div>
</section>

<div class="band"></div>

<!-- ===== lower presentation ===== -->
<section class="cover" style="left:162px;top:1586px;transform:scale(.79)">
  <div class="dark"></div>
  <div class="photo" role="img" aria-label="Foto: gedeckter Tisch am See mit Pasta, Pizza, Brotkorb und Rotwein"></div>
  <div class="brand-box">
    <div class="brand-name">Ufli</div>
    <div class="brand-sub">Seerestaurant – SEEBLICK – Seedorf</div>
  </div>
  <h1 class="title">Seerestaurant<br>SEEBLICK – Seedorf</h1>
  <div class="footer"><span class="addr">Uferweg 12 • 6000 Seedorf</span><span class="web">ufli-seedorf.ch</span></div>
</section>

<section class="spread" style="left:463px;top:1786px;transform:scale(.785)">
  <div class="page left">
    <div class="cream"></div>
    <div class="page-brand"><span class="dot"></span><div><div class="brand-name">Ufli</div><div class="brand-sub">Seerestaurant – SEEBLICK – Seedorf</div></div></div>
    <article class="card" style="top:111px;height:150px">
      <div class="pic" role="img" aria-label="Foto: Gulaschsuppe im Topf mit Brot" style="background:linear-gradient(150deg,#d8c39a,#8a3a22 55%,#3e2a20)"></div>
      <div class="name">GULASCHSUPPE</div><div class="desc">...die Echte – nach ungarischer Art</div>
      <div class="price"><span>kl. Portion CHF 13.50</span><span>gr. Portion CHF 20.50</span></div>
    </article>
    <article class="card" style="top:270px;height:143px">
      <div class="pic" role="img" aria-label="Foto: Salatteller mit Pouletstreifen" style="background:linear-gradient(150deg,#7e9a4a,#d9a24e 50%,#e8d27a 75%,#6a7a3a)"></div>
      <div class="name">FITNESSTELLER</div><div class="desc">mit Pouletstreifen</div>
      <div class="price"><span>CHF 13.50</span></div>
    </article>
    <p class="note">Alle Salate mit hausgemachter Salatsauce Ihrer Wahl und frischem Pizzabrot</p>
    <div class="panel" style="top:111px;height:126px">
      <h2>SUPPEN</h2>
      <div class="item"><b>BOUILLON</b> mit Tortellini<span class="cost">CHF 10.50</span></div>
      <div class="item"><b>MINESTRONE</b><span class="cost">CHF 11.50</span></div>
      <div class="item"><b>TAGESSUPPE</b> fragen Sie unser Personal<span class="cost">CHF 11.50</span></div>
    </div>
    <div class="panel" style="top:245px;height:225px">
      <h2>SALATE</h2>
      <div class="item"><b>BURRATA</b> italienischer Frischkäse, mit frischem Basilikum,<br>extra natives Olivenöl, Balsamico Crema und Cherry Tomaten<span class="cost">CHF 10.50</span></div>
      <div class="item"><b>CEASAR SALAT</b> mit Speck, Croûtons und Parmigiano DOP<span class="cost">CHF 10.50</span></div>
      <div class="item"><b>GEMISCHTER SALAT</b><span class="cost">CHF 10.50</span></div>
      <div class="item"><b>GRÜNER SALAT</b><span class="cost">CHF 10.50</span></div>
      <div class="item"><b>NÜSSLISALAT</b> mit Speck, Brotcroûtons und Ei<span class="cost">CHF 10.50</span></div>
      <div class="item"><b>SALAT «SEEBLICK»</b> Eisberg Salat, Speck, Croutons,<br>Parmigiano DOP und Pouletstreifen<span class="cost">CHF 10.50</span></div>
    </div>
  </div>
  <div class="page right">
    <div class="top-strip"></div>
    <div class="edge"></div>
    <article class="card" style="top:111px;height:150px">
      <div class="pic" role="img" aria-label="Foto: Chicken-Fingers mit Pommes und Dip" style="background:linear-gradient(150deg,#e8d6b0,#e6a63a 45%,#c8722e 70%,#f1ece0)"></div>
      <div class="name">CHICKEN-FINGERS</div><div class="desc">hausgemachte, panierte Pouletstreifen, dazu sweet Chili-Sauce und Pommes Frites</div>
      <div class="price"><span>CHF 32.50</span></div>
    </article>
    <article class="card" style="top:270px;height:151px">
      <div class="pic" role="img" aria-label="Foto: Pulled Pork Burger mit Pommes" style="background:linear-gradient(150deg,#6b4a34,#c8642e 45%,#e2b060 70%,#8a5a3a)"></div>
      <div class="name">PULLED PORK Burger</div><div class="desc">hausgemachte Bun, Pulled Pork (180g), BBQ-Sauce, Cheddar-Käse, Coleslaw (Kabissalat) und Jalapeno, serviert mit Pommes</div>
      <div class="price"><span>CHF 28.50</span></div>
    </article>
    <div class="panel" style="top:0;height:237px">
      <h2>HAUPTGERICHTE</h2>
      <div class="item"><b>BEEFSTEAK TARTAR</b> aus Schweizer-Qualitätsrindfleisch<br>abgeschmeckt nach Ihrem Wunsch, serviert mit Toastbrot und Butter<span class="cost">Vorspeise CHF 22.50 &nbsp;|&nbsp; Hauptgang CHF 32.50</span></div>
      <div class="item"><b>CORDON BLEU</b> «das Klassische» vom Schwein,<br>gefüllt mit Vorderschinken, Raclette und würzigem Gruyère<br>serviert mit Pommes Frites und Gemüse<span class="cost">CHF 26.50</span></div>
      <div class="item"><b>GYROS-TELLER</b> mit Schweinefleisch serviert mit Salat-Bouquet,<br>Tzatziki-Sauce und Pommes Frites<span class="cost">CHF 30.50</span></div>
      <div class="item"><b>WIENER SCHNITZEL</b> vom Kalb mit Pommes Frites<br>und Preiselbeeren<span class="cost">CHF 35.50</span></div>
    </div>
    <div class="panel" style="top:245px;height:225px">
      <h2>BARBECUE SPEZIALITÄTEN<br>AUS DEM SMOKER</h2>
      <div class="item"><b>BBQ SPARE RIBS</b> aus dem Smoker mit Cherry-Bomb Glasur<br>serviert mit Pommes frites<span class="cost">CHF 44.00</span></div>
      <div class="item"><b>PULLED BEEF Burger</b> Hausgemachte Bun, Pulled Beef (180g),<br>BBQ-Sauce, Cheddar-Käse, Coleslaw (Kabissalat) und Jalapeno,<br>serviert mit Pommes<span class="cost">CHF 31.50</span></div>
      <div class="item"><b>PULLED VEGI Burger</b> Hausgemachte Bun, BBQ-Sauce,<br>Cheddar-Käse, Coleslaw (Kabissalat) und Jalapeno, serviert mit Pommes<span class="cost">CHF 25.50</span></div>
      <p class="foot">Barbecue Gerichte werden 6-12 Stunden im Smoker gegart.<br>Wir verwenden ausschliesslich Schweizer Fleisch und<br>Bio Hickory Holz für das typische BBQ-Erlebnis<br>und Rauch-Aroma.</p>
    </div>
  </div>
</section>

</body>
</html>
```